Strategy plan/report for urban homeless shelter

Lay out a simple, 6-page report for a homeless shelter in San Jose, CA. Four statistics in the report need graphics. See style guide for color palette. EPS logo files included. Stock photography is available for use. Final strategy plan/report will be presented to board members, donors and foundations, so design needs to communicate need, concern (for the homeless) and hope for ending homelessness.

Target Market(s)

Tech executives who are board members and/or donors, as well as local foundations (e.g., the Velmont Foundation, the Draith Foundation).

Requirements
Must have
• Adhere to nonprofit's color palette (file attached).
• Graphical treatment of statistics.
• Agency's logo on front page. (file attached)
• Agency's url included: http://www.shelterbrookvx.org
Nice to have
• White space is good.
Should not have
• Report will be printed so please do not use black or dark background.

```html
<!DOCTYPE html>
<html lang="en">
<head>
<meta charset="UTF-8">
<title>Agency Strategic Plan 2016-2020 — Shelterbrook</title>
<link rel="stylesheet" href="https://fonts.googleapis.com/css2?family=Roboto+Condensed:wght@300;700&display=swap">
<style>
  :root {
    --paper: #f1f3f5;
    --scene-top: #e3e8ec;
    --scene-bottom: #eef1f3;
    --slate: #323f49;
    --accent-yellow: #e3a915;
    --brand-yellow: #f6bf2a;
    --band-white: #ffffff;
    --band-line: #dde2e6;
  }
  html, body {
    margin: 0;
    padding: 0;
    width: 873px;
    height: 1200px;
    overflow: hidden;
    background: var(--paper);
  }
  .cover {
    position: relative;
    width: 873px;
    height: 1200px;
    background: var(--paper);
    overflow: hidden;
    font-family: "Roboto Condensed", "Arial Narrow", sans-serif;
  }
  .cover-scene {
    position: absolute;
    left: 103px;
    top: 0;
    width: 738px;
    height: 861px;
    background: linear-gradient(160deg, var(--scene-top) 0%, var(--scene-bottom) 100%);
  }
  .cover-title {
    position: absolute;
    top: 420px;
    left: 0;
    width: 100%;
    margin: 0;
    text-align: center;
  }
  .cover-title .plan-name {
    display: block;
    font-weight: 300;
    font-size: 57px;
    letter-spacing: 0.5px;
    color: var(--slate);
    line-height: 1;
  }
  .cover-title .plan-years {
    display: block;
    margin-top: 32px;
    font-weight: 300;
    font-size: 53px;
    color: var(--accent-yellow);
    line-height: 1;
  }
  .brand-band {
    position: absolute;
    left: 0;
    top: 1008px;
    width: 100%;
    height: 127px;
    background: var(--band-white);
    border-top: 1px solid var(--band-line);
    border-bottom: 1px solid var(--band-line);
    box-sizing: border-box;
    display: flex;
    align-items: center;
    justify-content: center;
    gap: 16px;
  }
  .brand-mark {
    width: 40px;
    height: 40px;
    background: var(--brand-yellow);
  }
  .brand-name {
    font-weight: 700;
    font-size: 50px;
    color: var(--slate);
    line-height: 1;
  }
</style>
</head>
<body>
  <main class="cover">
    <div class="cover-scene" role="img" aria-label="Open doorway casting a long shadow of light across the floor"></div>

    <h1 class="cover-title">
      <span class="plan-name">AGENCY STRATEGIC PLAN</span>
      <span class="plan-years">2016-2020</span>
    </h1>

    <footer class="brand-band">
      <span class="brand-mark" aria-hidden="true"></span>
      <span class="brand-name">Shelterbrook</span>
    </footer>
  </main>
</body>
</html>
```